Reef Walk Harbour Tours poster template

Needing a series of signs to be designed, each based on a standard design as per the below.

The standard poster (measuring 2000mm high by 720mm wide) will be located on a door that some 400k individuals will be walking past. The poster needs to be able to stop a very significant proportion of these individuals in their tracks, and motivate them to come over and read more.

What does the poster advertise? Our tours. Reef Walk Harbour Tours offers underwater walking tours in dive helmets off the end of the iconic Marrowby Pier, 1.8kms out from the shore.

The final design must be
1. visually striking / GRAB attention
2. be very simple and easy to make sense of all information on it
3. and communicate wonder / excitement / fun.

A mockup of the basic layout for the poster is attached showing headlines and copy required:
- size of font, and relative size of items within the sign v much up to you to decide - as long as achieve requirements above.
- High rez files for all images used are available.
- Female seawalker needs to be superimposed on background that has the the two jetty pylons covered in colourful corals. (Existing diver in these photos to be replaced.)
- Suggesting photos may work within an oval frame - seen something similar and liked the "dreamlike" feel it added.
- Wanting photos to dominate the sign / be the focus of the sign / be as big as possible whilst ensuring headlines and copy easy to read / make sense of.

Target Market(s)

Broadly, almost all 12-80 year olds living in or visiting the South West region of Western Australia
Focussed, visitors to the Marrowby Pier each day.

Industry/Entity Type

Tourism

Font styles to use
Sans Serif

Requirements
Must have
• a design that GRABS attention of passers by
• have copy that is easy to read and v clear to understand
• motivate people to contact us
Should not have
• Anything that distracts from copy or photo of tour participant

```html
<!DOCTYPE html>
<html lang="en">
<head>
<meta charset="utf-8">
<title>Reef Walk Harbour Tours – Go Below! Poster</title>
<link rel="stylesheet" href="https://fonts.googleapis.com/css2?family=Arimo:ital,wght@0,700;1,700&display=swap">
<style>
  :root {
    --white: #ffffff;
    --navy: #0f2f66;
    --navy-deep: #0a2452;
    --sky: #d6ecf8;
    --sea-light: #8fc8ec;
    --cyan: #1496d8;
    --headline: #123a78;
    --yellow: #ffe500;
    --panel: rgba(120, 150, 190, 0.55);
    --coral: #d98a3a;
    --reef-teal: #2e8fb0;
  }
  html, body {
    margin: 0;
    padding: 0;
    width: 1200px;
    height: 3332px;
    overflow: hidden;
    background: var(--white);
  }
  .poster {
    position: relative;
    width: 1200px;
    height: 3332px;
    overflow: hidden;
    font-family: "Arimo", Arial, sans-serif;
    background: linear-gradient(180deg,
      var(--white) 0px, var(--white) 360px,
      var(--sky) 520px, var(--sea-light) 860px,
      var(--reef-teal) 1600px, var(--navy) 2200px,
      var(--navy-deep) 3332px);
  }
  .brand {
    position: absolute;
    top: 60px;
    left: 0;
    width: 100%;
    text-align: center;
    color: var(--headline);
    font-weight: 700;
    font-size: 96px;
    line-height: 1;
  }
  .brand-sub {
    display: block;
    margin-top: 18px;
    font-size: 48px;
    letter-spacing: 4px;
  }
  .water-surface {
    position: absolute;
    top: 370px;
    left: 0;
    width: 1200px;
    height: 90px;
    background: linear-gradient(180deg, #cfe6f4 0%, #7fb6dc 45%, #e3f1fa 100%);
  }
  .headline {
    position: absolute;
    top: 520px;
    left: 0;
    width: 100%;
    margin: 0;
    text-align: center;
    color: var(--headline);
    font-style: italic;
    font-weight: 700;
    font-size: 196px;
    line-height: 1;
    letter-spacing: -4px;
  }
  .subhead {
    position: absolute;
    top: 720px;
    left: 0;
    width: 100%;
    margin: 0;
    text-align: center;
    color: var(--cyan);
    font-style: italic;
    font-weight: 700;
    font-size: 78px;
    line-height: 1;
  }
  .hero-photo {
    position: absolute;
    top: 850px;
    left: 0;
    width: 1200px;
    height: 1340px;
    background:
      radial-gradient(ellipse 38% 30% at 52% 42%, #cfe8f4 0%, #7cc0e0 55%, transparent 80%),
      linear-gradient(90deg, var(--coral) 0%, #6aa9c6 30%, #4fa6d0 70%, var(--coral) 100%);
    -webkit-mask-image: linear-gradient(180deg, transparent 0%, #000 8%, #000 90%, transparent 100%);
    mask-image: linear-gradient(180deg, transparent 0%, #000 8%, #000 90%, transparent 100%);
  }
  .tagline {
    position: absolute;
    top: 2220px;
    left: 60px;
    width: 1080px;
    transform: rotate(-3deg);
    text-align: center;
    color: var(--white);
  }
  .tagline-rule {
    height: 4px;
    background: var(--white);
    margin: 0 20px;
  }
  .tagline-text {
    margin: 22px 0;
    font-style: italic;
    font-weight: 700;
    font-size: 62px;
    line-height: 1.15;
  }
  .benefits {
    position: absolute;
    top: 2470px;
    left: 100px;
    margin: 0;
    padding: 0;
    list-style: none;
  }
  .benefit {
    display: flex;
    align-items: center;
    height: 110px;
    color: var(--yellow);
    font-weight: 700;
    font-size: 66px;
  }
  .benefit svg {
    width: 76px;
    height: 76px;
    margin-right: 32px;
    flex: none;
  }
  .booking {
    position: absolute;
    top: 2800px;
    left: 88px;
    width: 1060px;
    height: 300px;
    box-sizing: border-box;
    padding-top: 30px;
    border-radius: 14px;
    background: var(--panel);
    text-align: center;
    color: var(--white);
    font-weight: 700;
  }
  .booking-title {
    margin: 0 0 14px;
    font-size: 56px;
  }
  .booking-line {
    margin: 0;
    font-size: 50px;
    line-height: 1.3;
  }
  .booking-line .highlight { color: var(--yellow); }
  .operator {
    position: absolute;
    top: 3170px;
    left: 0;
    width: 100%;
    display: flex;
    justify-content: center;
    align-items: center;
    color: var(--white);
    font-weight: 700;
    font-size: 40px;
  }
  .operator-dot {
    width: 44px;
    height: 44px;
    border-radius: 50%;
    background: var(--white);
    margin-right: 18px;
  }
</style>
</head>
<body>
<div class="poster">
  <div class="brand">DeepStride<span class="brand-sub">HELMET DIVING</span></div>
  <div class="water-surface" role="img" aria-label="Rippling sea surface seen from just below the water"></div>

  <h1 class="headline">Go Below!</h1>
  <p class="subhead">Walk under the sea today!</p>

  <div class="hero-photo" role="img" aria-label="Smiling woman in a clear dive helmet among colourful corals on pier pylons, with yellow and blue tropical fish"></div>

  <div class="tagline">
    <div class="tagline-rule"></div>
    <p class="tagline-text">See the underwater&nbsp; wonderland<br>beneath the Jetty for yourself!</p>
    <div class="tagline-rule"></div>
  </div>

  <ul class="benefits">
    <li class="benefit">
      <svg viewBox="0 0 40 40" aria-hidden="true"><path d="M4 22 L15 33 L37 6" fill="none" stroke="#ffffff" stroke-width="6" stroke-linecap="round" stroke-linejoin="round"/></svg>
      Very safe and easy to do
    </li>
    <li class="benefit">
      <svg viewBox="0 0 40 40" aria-hidden="true"><path d="M4 22 L15 33 L37 6" fill="none" stroke="#ffffff" stroke-width="6" stroke-linecap="round" stroke-linejoin="round"/></svg>
      For (nearly) everyone 12-70+
    </li>
    <li class="benefit">
      <svg viewBox="0 0 40 40" aria-hidden="true"><path d="M4 22 L15 33 L37 6" fill="none" stroke="#ffffff" stroke-width="6" stroke-linecap="round" stroke-linejoin="round"/></svg>
      No diving experience needed
    </li>
  </ul>

  <div class="booking">
    <p class="booking-title">How to book onto today’s tours:</p>
    <p class="booking-line">Book online at <span class="highlight">www.harbourseawalks.com</span></p>
    <p class="booking-line">Or book by phone on <span class="highlight">1 800 555 014</span></p>
  </div>

  <div class="operator"><span class="operator-dot"></span>Reef Walk Harbour Tours</div>
</div>
</body>
</html>
```